Flyer für Verkauf von Radondetektoren
Zielgruppe
Ich verkaufe Radondetektoren zur Messung von Radon in Innenräumen. Zielgruppe sind Privatpersonen, Firmen, Genossenschaften und andere Hauseigentümer.
Aufgabenstellung
Ich brauche das Design für meine Messanleitung.
Kreativ - modern - weniger kann mehr sein
Struktur ist wichtigt, es soll also einfach sein zu lesen und zu verstehen, was gemacht werden soll. Können Bulletpoints, Icons mit eingebracht werden.
Wichtig ist auch, dass die beiden Logos 'Luftprüfer.de' und KALVORIX' auf der Messanleitung vorhanden sind. Wobei 'Luftprüfer.de' das Hauptlogo ist.
DIN format dachte ich A4 beidseitig (Text müsste also auf diese Grösse angepasst werden).
Kann natürlich auch Flyer-Format sein oder andere Vorschläge!
Bildmaterial gibt es auf unsere Homepage https://luftprüfer.de und https://luftkollen.se . Diese haben wir bereits gekauft und können verwendet werden. Ich lade sie den bei Bedarf hoch. Es können natürlich auch andere Vorschläge kommen.

```html
<!DOCTYPE html>
<html lang="de">
<head>
<meta charset="utf-8">
<title>Messanleitung Radonmessung</title>
<link href="https://fonts.googleapis.com/css2?family=Barlow:ital,wght@0,400;0,500;1,400&family=Roboto:ital,wght@0,700;0,900;1,700&display=swap" rel="stylesheet">
<style>
  :root{
    --red:#e2121b;
    --ink:#3c3c3c;
    --text:#3a3a3a;
    --band-light:#efefef;
    --band-dark:#bdbdbd;
    --white:#ffffff;
  }
  *{margin:0;padding:0;box-sizing:border-box;}
  html,body{width:1200px;height:848px;overflow:hidden;background:var(--white);}
  body{position:relative;font-family:"Barlow",sans-serif;color:var(--text);font-size:13.6px;line-height:18.6px;}
  .abs{position:absolute;}
  p{text-align:justify;}

  /* step bands */
  .step-band{left:0;width:330px;height:60px;
    background:
      repeating-linear-gradient(120deg,rgba(255,255,255,.35) 0 2px,transparent 2px 6px),
      linear-gradient(90deg,var(--band-light),var(--band-dark));}
  .step-label{left:24px;font-family:"Roboto",sans-serif;color:var(--ink);}
  .step-label b{font-size:30px;font-weight:900;}
  .step-label span{font-size:19px;letter-spacing:1px;font-weight:400;font-family:"Barlow",sans-serif;}
  .step-badge{width:66px;height:66px;border-radius:50%;background:var(--red);border:4px solid var(--white);
    display:flex;flex-direction:column;align-items:center;justify-content:center;color:var(--white);}
  .step-badge small{font-family:"Roboto",sans-serif;font-weight:900;font-size:9px;letter-spacing:.4px;margin-top:1px;}

  .section-title{font-family:"Roboto",sans-serif;font-weight:900;color:var(--ink);font-size:26.5px;line-height:33px;letter-spacing:.3px;}

  .portal-link{left:36px;top:249px;width:332px;height:38px;border-radius:19px;background:var(--red);
    color:var(--white);font-family:"Roboto",sans-serif;font-weight:700;font-size:15.5px;line-height:38px;padding-left:18px;}
  .pointer{left:314px;top:258px;}

  .note{font-style:italic;}

  .intro{left:482px;top:36px;font-family:"Roboto",sans-serif;font-weight:700;font-style:italic;font-size:16.5px;line-height:21px;color:var(--ink);}

  .sub-title{font-family:"Roboto",sans-serif;font-weight:700;color:var(--red);font-size:16.5px;line-height:19px;}

  .checklist{list-style:none;}
  .checklist li{position:relative;padding-left:21px;text-align:justify;}
  .checklist li::before{content:"»";position:absolute;left:0;top:-3px;color:var(--red);font-family:"Roboto",sans-serif;font-weight:700;font-size:21px;}

  .contact{left:511px;top:773px;font-family:"Roboto",sans-serif;font-style:italic;font-weight:700;color:var(--red);font-size:16px;line-height:21px;}
  .contact .hours{font-family:"Barlow",sans-serif;font-weight:400;}
</style>
</head>
<body>

<!-- Column 1: Schritt 1 -->
<div class="abs step-band" style="top:28px;"></div>
<div class="abs step-label" style="top:38px;"><b>1.</b> <span>SCHRITT</span></div>
<div class="abs step-badge" style="left:313px;top:25px;">
  <svg width="26" height="22" viewBox="0 0 26 22" aria-hidden="true"><circle cx="10" cy="5.5" r="5" fill="#fff"/><path d="M0 21c0-6 4-9 10-9s8 2 9 4v5z" fill="#fff"/><circle cx="20" cy="15" r="5.5" fill="#fff"/><rect x="17.3" y="14.5" width="5.4" height="4" rx=".6" fill="#e2121b"/><path d="M18.3 14.5v-1.3a1.7 1.7 0 013.4 0v1.3" stroke="#e2121b" stroke-width="1" fill="none"/></svg>
  <small>LOGIN</small>
</div>

<h2 class="abs section-title" style="left:24px;top:111px;">REGISTRIERUNG<br>UND ANMELDUNG</h2>
<p class="abs" style="left:24px;top:191px;width:356px;">Wenn Sie Neukunde sind, legen Sie bitte zunächst ein neues Benutzerkonto auf unserem Online-Portal an:</p>

<div class="abs portal-link">https://kundenportal.kalvorix.se/de</div>
<svg class="abs pointer" width="40" height="52" viewBox="0 0 40 52" aria-hidden="true">
  <g stroke="#e2121b" stroke-width="1.5" fill="none"><path d="M15 2v5M7 6l3 3M23 6l-3 3M4 13h4M22 13h4"/></g>
  <path d="M12 44c-4-4-9-10-8-13 1-2 4-1 6 2V13a3 3 0 016 0v10a3 3 0 015 0v2a3 3 0 015 0v2a3 3 0 015 0v9c0 6-3 10-8 10h-7c-2 0-3-1-4-2z" fill="#fff" stroke="#3c3c3c" stroke-width="2" stroke-linejoin="round"/>
</svg>

<p class="abs" style="left:24px;top:322px;width:356px;">Anschließend können Sie die Radondetektoren registrieren. Vermerken Sie den Start der Messung (Datum und Uhrzeit), die Messorte (Raum und Etage) sowie die 9-stellige Seriennummer der Detektoren, die Sie auf der Verpackung oder auf der Unterseite der jeweiligen Detektoren finden.</p>
<p class="abs note" style="left:24px;top:433px;width:356px;">Firmenkunden haben die Möglichkeit eine Excel-Datei als Hilfsmittel herunterzuladen, die Sie ausfüllen und dann wieder hochladen.</p>

<!-- Column 1: Schritt 2 -->
<div class="abs step-band" style="top:512px;"></div>
<div class="abs step-label" style="top:522px;"><b>2.</b> <span>SCHRITT</span></div>
<div class="abs step-badge" style="left:313px;top:509px;">
  <svg width="24" height="32" viewBox="0 0 24 32" aria-hidden="true"><path d="M12 31C5 21 1 16 1 11a11 11 0 0122 0c0 5-4 10-11 20z" fill="#fff"/><circle cx="12" cy="11" r="4.2" fill="#e2121b"/></svg>
</div>

<h2 class="abs section-title" style="left:24px;top:594px;">PLATZIERUNG<br>DER DETEKTOREN</h2>
<p class="abs" style="left:24px;top:674px;width:356px;">Bevor Sie die Detektoren der Verpackung entnehmen, überlegen Sie wo genau Sie die Radondetektoren platzieren wollen. Die Radonmessung beginnt, sobald Sie die radondichten Verpackungen öffnen. Beachten Sie bei der Platzierung zunächst die Auswahl der Räume und die Positionierung der Radondetektoren im Raum.</p>

<!-- Column 2 -->
<svg class="abs" style="left:429px;top:33px;" width="46" height="44" viewBox="0 0 46 44" aria-hidden="true">
  <rect x="2.5" y="8.5" width="32" height="32" rx="4" fill="none" stroke="#e2121b" stroke-width="5"/>
  <path d="M10 22l8 8L42 3" fill="none" stroke="#e2121b" stroke-width="6" stroke-linecap="round" stroke-linejoin="round"/>
</svg>
<div class="abs intro">Für eine zuverlässige Radonmessung<br>empfehlen wir wie folgt vorzugehen:</div>

<h2 class="abs section-title" style="left:429px;top:111px;">AUSWAHL DER RÄUME</h2>

<svg class="abs" style="left:429px;top:154px;" width="45" height="36" viewBox="0 0 45 36" aria-hidden="true">
  <path d="M2 16L22.5 3 43 16" fill="none" stroke="#e2121b" stroke-width="3.5" stroke-linejoin="round"/>
  <path d="M7 15L22.5 6 38 15v21H7z" fill="#e2121b"/>
  <rect x="12" y="21" width="8" height="8" fill="#fff"/><rect x="24" y="21" width="8" height="15" fill="#fff"/>
</svg>
<h3 class="abs sub-title" style="left:480px;top:172px;">Einfamilienhäuser</h3>
<ul class="abs checklist" style="left:429px;top:210px;width:356px;">
  <li>Es sollten mindestens zwei Wohnräume und pro bewohnte Etage mindestens ein Wohnraum gemessen werden. Wählen Sie Räume aus, in denen Sie sich oft aufhalten (z.B. das Wohn- und Schlafzimmer). Vermeiden Sie aber Räume, in denen das Fenster mehrere Stunden am Tag oder in der Nacht geöffnet ist.</li>
  <li>Insofern Sie einen Keller haben, empfehlen wir alle Kellerräume zu messen, da hier meist das größte Risiko einer erhöhten Radonkonzentration erwartet wird.</li>
</ul>

<svg class="abs" style="left:429px;top:393px;" width="45" height="57" viewBox="0 0 45 57" aria-hidden="true">
  <path d="M2 14L22.5 2 43 14" fill="none" stroke="#e2121b" stroke-width="3.5" stroke-linejoin="round"/>
  <path d="M6 13L22.5 5 39 13v44H6z" fill="#e2121b"/>
  <g fill="#fff"><rect x="12" y="18" width="8" height="7"/><rect x="24" y="18" width="8" height="7"/><rect x="12" y="29" width="8" height="7"/><rect x="24" y="29" width="8" height="7"/><rect x="12" y="40" width="8" height="7"/><rect x="24" y="40" width="8" height="7"/></g>
</svg>
<h3 class="abs sub-title" style="left:480px;top:413px;">Mehrfamilienhäuser, Wohnungen<br>und Wohnkomplexen</h3>
<ul class="abs checklist" style="left:429px;top:470px;width:356px;">
  <li>Alle Wohnungen mit direktem Bodenkontakt sowie mindestens eine Wohnung pro Etage sollten gemessen werden. Wählen Sie dabei Wohnungen, die an Aufzügen oder Luftschächten liegen.</li>
  <li>In größeren Wohnkomplexen sollten insgesamt mindestens 20&nbsp;% aller Wohnungen in einem Gebäude gemessen werden.</li>
  <li>Es sollten mindestens zwei Wohnräume pro ausgewählte Wohnung gemessen werden. Wählen Sie Räume aus, in denen Sie sich oft aufhalten (z.B. das Wohn- und Schlafzimmer). Vermeiden Sie aber Räume, in denen das Fenster mehrere Stunden am Tag oder in der Nacht geöffnet ist.</li>
  <li>Selbst bei einer Einzimmerwohnung sollten Sie zwei Detektoren aufstellen.</li>
</ul>

<svg class="abs" style="left:429px;top:774px;" width="60" height="54" viewBox="0 0 60 54" aria-hidden="true">
  <path d="M2 2h56v36H30l-8 12-2-12H2z" fill="none" stroke="#e2121b" stroke-width="2.5" stroke-linejoin="round"/>
  <circle cx="20" cy="16" r="1.8" fill="#e2121b"/><circle cx="40" cy="16" r="1.8" fill="#e2121b"/>
  <path d="M22 25q8 7 16 0" fill="none" stroke="#e2121b" stroke-width="2.2" stroke-linecap="round"/>
</svg>
<div class="abs contact">Wenn Sie noch Fragen haben, rufen Sie uns an. Wir sind Ihnen gern behilflich.<br>Telefon +49 (0) 176 555 012 34 &nbsp;<span class="hours">Mo - Fr / 13 - 15 Uhr</span></div>

<!-- Column 3 -->
<svg class="abs" style="left:834px;top:63px;" width="36" height="53" viewBox="0 0 36 53" aria-hidden="true">
  <rect x="0" y="0" width="36" height="3" fill="#e2121b"/><rect x="0" y="5" width="36" height="48" fill="#e2121b"/>
  <g fill="#fff"><rect x="4" y="16" width="7" height="6"/><rect x="14.5" y="16" width="7" height="6"/><rect x="25" y="16" width="7" height="6"/><rect x="4" y="25" width="7" height="6"/><rect x="14.5" y="25" width="7" height="6"/><rect x="25" y="25" width="7" height="6"/><rect x="4" y="34" width="7" height="6"/><rect x="14.5" y="34" width="7" height="6"/><rect x="25" y="34" width="7" height="6"/></g>
</svg>
<h3 class="abs sub-title" style="left:884px;top:98px;">Arbeitsplätze und öffentliche Gebäude</h3>
<ul class="abs checklist" style="left:834px;top:136px;width:344px;">
  <li>Wählen Sie Räume, die regelmäßig mehr als vier Stunden pro Tag genutzt werden.</li>
  <li>Messen Sie alle unterirdischen Räumlichkeiten, da hier meist das größte Risiko einer erhöhten Radonkonzentration erwartet wird.</li>
  <li>Messen Sie alle Räume im Erdgeschoß. Für größere Räumlichkeiten empfehlen wir einen Detektor pro 200 m².</li>
  <li>In den oberen Etagen sollten Sie mit mindestens zwei Detektoren, sowie mindestens einem Detektor pro 200 m² messen.</li>
  <li>Falls Ihr Arbeitsplatz in einem Radon-Vorsorgegebiet liegt und somit der Messpflicht unterliegt, muss die Messdauer von 12 Monaten eingehalten werden.</li>
</ul>

<svg class="abs" style="left:834px;top:400px;" width="43" height="33" viewBox="0 0 43 33" aria-hidden="true">
  <rect x="1" y="1" width="41" height="31" fill="none" stroke="#e2121b" stroke-width="2"/>
  <rect x="5" y="5" width="33" height="23" fill="none" stroke="#e2121b" stroke-width="1.5"/>
  <path d="M1 1l4 4M42 1l-4 4M1 32l4-4M42 32l-4-4" stroke="#e2121b" stroke-width="1.5"/>
  <rect x="13" y="11" width="8" height="6" fill="none" stroke="#e2121b" stroke-width="1.5"/>
</svg>
<h3 class="abs sub-title" style="left:884px;top:413px;">Platzierung der Detektoren im Raum</h3>
<ul class="abs checklist" style="left:834px;top:451px;width:344px;">
  <li>Platzieren Sie die Detektoren in einem Mindestabstand von 20 cm zu Wänden, 50 cm zu Abluftsventilen, sowie 1,50 m zu Fenstern, Außentüren, Zuluftsventilen und Heizkörpern.</li>
  <li>Stellen Sie die Detektoren nicht auf dem Boden, an starken Wärmequellen oder Luftströmen auf. Vermeiden Sie auch Räume mit hoher Luftfeuchtigkeit, wie zum Beispiel das Badezimmer.</li>
  <li>Die Detektoren können entweder stehend (auf einem Tisch, im Regal oder einer Schrankwand) oder hängend mitten im Raum (z.B. von einer Lampe) platziert werden.</li>
  <li>Stellen Sie die Detektoren während der gesamten Messdauer nicht um.</li>
  <li>Versuchen Sie nicht das Gehäuse der Detektoren zu öffnen und platzieren Sie diese immer außer Reichweite von Kindern.</li>
</ul>

</body>
</html>
```